Meadowlark Dental Letterhead

Please design full color letterhead for meadowlark dental. Letterhead should match the motif of the business card. Print and logo should be confined to a one inch margin on top and bottom. The following info should be included:
Meadowlrk Dental with the tooth logo
Curtis R. Holloway, DDS
Gentle Hands, Bright Smiles Daily
Phone #: 918.555.0147
Address: 24813-C N Sycamore, Bixby, OK

```html
<!DOCTYPE html>
<html lang="en">
<head>
<meta charset="utf-8">
<title>Meadowlark Dental Letterhead</title>
<link href="https://fonts.googleapis.com/css2?family=Montserrat:wght@400;600;700&display=swap" rel="stylesheet">
<style>
  :root {
    --navy: #1c3f8f;
    --blue: #2a5bb8;
    --ink: #333a44;
    --red: #d8262b;
    --green: #3aa63e;
    --paper: #ffffff;
    --faint-square: #dfe6f2;
    --faint-text: #c5d0e3;
  }
  html, body {
    margin: 0;
    padding: 0;
    width: 847px;
    height: 1200px;
    overflow: hidden;
    background: var(--paper);
  }
  .letterhead {
    position: relative;
    width: 847px;
    height: 1200px;
    background: var(--paper);
    font-family: "Montserrat", sans-serif;
    color: var(--ink);
  }
  .brand {
    position: absolute;
    left: 56px;
    top: 52px;
    width: 240px;
    text-align: center;
  }
  .brand-square {
    width: 52px;
    height: 52px;
    margin: 0 auto 14px;
    background: var(--blue);
  }
  .brand-name {
    margin: 0;
    font-weight: 700;
    font-size: 30px;
    line-height: 1.05;
    letter-spacing: 0.5px;
    color: var(--navy);
    text-transform: uppercase;
  }
  .brand-tagline {
    margin: 8px 0 0;
    font-size: 8.5px;
    font-weight: 600;
    letter-spacing: 0.3px;
    color: var(--navy);
    text-transform: uppercase;
  }
  .watermark {
    position: absolute;
    left: 508px;
    top: 762px;
    width: 240px;
    height: 240px;
    background: var(--faint-square);
    opacity: 0.6;
    display: flex;
    align-items: flex-end;
    justify-content: center;
  }
  .watermark-name {
    margin: 0 0 18px;
    font-weight: 700;
    font-size: 22px;
    color: var(--faint-text);
    text-transform: uppercase;
  }
  .contact {
    position: absolute;
    left: 56px;
    top: 990px;
    font-size: 13px;
    line-height: 1.2;
  }
  .contact-name {
    margin: 0 0 12px;
    font-weight: 700;
    font-size: 15px;
    color: var(--blue);
  }
  .contact-line {
    margin: 0 0 10px;
    display: flex;
    align-items: center;
    gap: 6px;
  }
  .contact-phone { font-size: 15px; }
  .contact-web { font-size: 11px; }
  .phone-icon { width: 17px; height: 14px; }
  .footer-band {
    position: absolute;
    left: 0;
    top: 1100px;
    width: 847px;
    height: 100px;
    background: linear-gradient(to bottom,
      rgba(216, 38, 43, 0) 0%,
      rgba(216, 38, 43, 0.35) 18%,
      rgba(42, 91, 184, 0.45) 38%,
      var(--green) 55%,
      var(--green) 100%);
  }
  .footer-slogan {
    position: absolute;
    right: 36px;
    bottom: 22px;
    margin: 0;
    color: #fff;
    font-weight: 600;
    font-size: 21px;
  }
</style>
</head>
<body>
<div class="letterhead">
  <header class="brand">
    <div class="brand-square"></div>
    <h1 class="brand-name">Meadowlark<br>Dental</h1>
    <p class="brand-tagline">Gentle Hands, Bright Smiles Daily</p>
  </header>

  <div class="watermark" aria-hidden="true">
    <p class="watermark-name">Meadowlark</p>
  </div>

  <section class="contact">
    <p class="contact-name">Curtis R. Holloway, D.D.S.</p>
    <p class="contact-line contact-phone">
      <svg class="phone-icon" viewBox="0 0 24 20" aria-hidden="true">
        <path d="M2 6c0-3 4-5 10-5s10 2 10 5v2h-5V6c-2-1-8-1-10 0v2H2z" fill="var(--navy)"/>
        <path d="M6 9h12l3 9H3z" fill="var(--navy)"/>
        <circle cx="12" cy="13.5" r="2.4" fill="#fff"/>
      </svg>
      918-555-0147
    </p>
    <p class="contact-line">24813-C North Sycamore, Cedar Bend, OK 74120</p>
    <p class="contact-line contact-web">www.meadowlarkdentalok.com</p>
  </section>

  <div class="footer-band" role="img" aria-label="Decorative footer band in red, blue and green"></div>
  <p class="footer-slogan">For ALL Your Dental Needs</p>
</div>
</body>
</html>
```